Online Course Page

We are building a video based online course page. This project is for only the actual page that the student will watch the videos at. They will watch one vide at a time. Once one video lesson is completed then they can move to the next video lesson. The page will need to show the video player. (Main feature.) The list of lessons in the course. Instructor information. Profile picture and bio of the instructor. A Live chat button that will initiate a chat in real-time with the instructor.

The winning designer will also be asked to to design the dashboard area and other aspects of the user interface as an additional project.

Target Market(s)

Adults

Number of Pages Required

1 page

Colors
9bcb3c

Requirements
Must have
• Our logo is attached. Green and grey are our colors. Should feel modern, clean and be simple to navigate. The site will be responsive so the layout should work well on mobile devices.

```html
<!DOCTYPE html>
<html lang="en">
<head>
<meta charset="utf-8">
<title>LessonHall – Course Player</title>
<link rel="stylesheet" href="https://fonts.googleapis.com/css2?family=Varela+Round&family=Open+Sans:wght@400;600;700&display=swap">
<style>
:root{
  --green:#8dc63f;
  --teal:#45d6c2;
  --ink:#1a1a1a;
  --grey-panel:#efefef;
  --grey-line:#d6d6d6;
  --footer:#000;
  --white:#fff;
}
*{box-sizing:border-box;margin:0;padding:0}
h1,h2,h3{font-weight:400}
html,body{width:814px;height:1200px;overflow:hidden;background:var(--white)}
body{position:relative;font-family:"Open Sans",sans-serif;color:var(--ink)}
.page{position:relative;width:814px;height:1200px;overflow:hidden}
.abs{position:absolute}

.hero-bg{left:0;top:0;width:814px;height:680px;
  background:linear-gradient(170deg,#dcdcdc 0%,#e8e8e8 35%,#f4f4f4 55%,rgba(255,255,255,0) 75%)}
.hero-photo{left:0;top:0}
.brand{left:136px;top:124px;display:flex;align-items:center;gap:8px;
  font-family:"Varela Round",sans-serif;font-size:19px;color:var(--green)}
.brand-dot{width:20px;height:20px;border-radius:50%;background:var(--green)}
.hero-title{left:142px;top:204px;font-family:"Varela Round",sans-serif;font-size:29px;line-height:32px;letter-spacing:.5px}
.hero-sub{left:144px;top:232px;font-size:9.6px;font-weight:600}
.btn-signup{left:218px;top:249px;width:83px;height:15px;background:var(--teal);color:#fff;
  font-size:9px;font-weight:600;text-align:center;line-height:15px;text-decoration:none}

.course-title{left:0;width:834px;top:480px;text-align:center;font-family:"Varela Round",sans-serif;font-size:16.5px}
.course-section{left:0;width:834px;top:501px;text-align:center;font-size:9px;color:var(--teal)}

.player{left:84px;top:542px;width:330px;height:219px;
  background:linear-gradient(135deg,#4a4238 0%,#6a5f52 45%,#8d8a84 100%)}
.player-label{left:208px;top:630px;color:#fff;font-size:29px;line-height:27px}
.control-band{left:0;top:761px;width:814px;height:28px;background:var(--green)}
.controls{left:84px;top:761px;width:330px;height:28px;background:linear-gradient(#e6e6e6,#d4d4d4)}
.band-instructor{left:426px;top:772px;font-size:7.2px;font-weight:700;color:#fff}
.band-instructor a{color:#fff}
.band-count{left:634px;top:769px;font-size:9px;font-weight:700;color:#fff}

.lesson-head{left:440px;top:552px;font-family:"Varela Round",sans-serif;font-size:14px;color:var(--green)}
.lesson-desc{left:461px;top:574px;width:262px;font-size:7.6px;line-height:9.6px}
.lesson-item{left:440px;top:638px;width:284px;height:56px;background:var(--grey-panel);border-left:6px solid var(--green)}
.lesson-item p{position:absolute;left:15px;top:12px;width:262px;font-size:7.6px;line-height:9.6px}
.lesson-item .row{position:absolute;left:0;right:0;top:38px;border-top:1px solid var(--grey-line);
  display:flex;justify-content:space-between;padding:4px 10px 0 16px;font-size:7.4px;color:var(--green)}

.coach-photo{left:118px;top:820px}
.coach-kicker{left:403px;top:828px;font-family:"Varela Round",sans-serif;font-size:12.5px}
.coach-role{left:403px;top:841px;font-family:"Varela Round",sans-serif;font-size:20px;color:var(--green);letter-spacing:.5px}
.coach-name{left:403px;top:868px;font-family:"Varela Round",sans-serif;font-size:14px}
.coach-name b{font-weight:400;font-size:19px}
.coach-stars{left:409px;top:906px}
.coach-bio{left:415px;top:960px;width:310px;font-size:7.6px;line-height:9.6px}
.coach-link{left:415px;top:1008px;font-size:7.6px;color:var(--ink)}

.footer{left:0;top:1128px;width:814px;height:72px;background:var(--footer);color:#fff}
.social{position:absolute;left:342px;top:20px;display:flex;gap:10px}
.social span{width:14px;height:14px;border-radius:50%;background:#fff;display:block}
.copyright{position:absolute;left:0;width:814px;top:46px;text-align:center;font-size:7.6px}
</style>
</head>
<body>
<main class="page">

  <section class="hero">
    <div class="abs hero-bg"></div>
    <svg class="abs hero-photo" width="814" height="440" viewBox="0 0 814 440" role="img" aria-label="Photo of a laughing man with glasses">
      <defs>
        <linearGradient id="photoTone" x1="0" y1="0" x2="1" y2="1">
          <stop offset="0" stop-color="#5a4a42"/>
          <stop offset=".5" stop-color="#8a7468"/>
          <stop offset="1" stop-color="#c8c2bc"/>
        </linearGradient>
      </defs>
      <polygon points="296,0 814,0 814,190 765,262 700,380 600,418 430,420 296,180" fill="url(#photoTone)"/>
    </svg>
    <div class="abs brand"><span class="brand-dot"></span>LessonHall</div>
    <h1 class="abs hero-title">WE CARE</h1>
    <p class="abs hero-sub">ABOUT YOUR UPCOMING COURSES</p>
    <a class="abs btn-signup" href="#">SIGN UP NOW</a>
  </section>

  <section class="course">
    <h2 class="abs course-title">NAME OF COURSE RIGHT NOW</h2>
    <p class="abs course-section">SECTION 2</p>

    <div class="abs player" role="img" aria-label="Video frame: desk with papers, laptop and a plant, seen from above"></div>
    <p class="abs player-label">sculpt<br>course</p>

    <div class="abs control-band"></div>
    <div class="abs controls">
      <svg width="330" height="28" viewBox="0 0 330 28">
        <rect x="32" y="10" width="2" height="7" fill="#222"/><rect x="36" y="10" width="2" height="7" fill="#222"/>
        <polygon points="55,10 62,13.5 55,17" fill="#222"/>
        <rect x="78" y="10" width="7" height="7" fill="#222"/>
        <path d="M286 10h2M286 10v2M294 10h-2M294 10v2M286 17h2M286 17v-2M294 17h-2M294 17v-2" stroke="#222" stroke-width="1.4" fill="none"/>
        <path d="M311 11a4 4 0 1 0 1.5 3" stroke="#222" stroke-width="1.6" fill="none"/>
        <polygon points="310,8 314,11 310,13" fill="#222"/>
      </svg>
    </div>
    <p class="abs band-instructor">INESTRACTOR: <a href="#">MARK ELLISON</a></p>
    <p class="abs band-count">NU 01 OF 13</p>
    <svg class="abs" style="left:710px;top:767px" width="20" height="16" viewBox="0 0 20 16">
      <g fill="#fff"><circle cx="2" cy="2" r="1.6"/><circle cx="2" cy="8" r="1.6"/><circle cx="2" cy="14" r="1.6"/>
      <rect x="6" y="1" width="13" height="2"/><rect x="6" y="7" width="13" height="2"/><rect x="6" y="13" width="13" height="2"/></g>
    </svg>

    <h3 class="abs lesson-head">01. NAME OF ACTIVATED VIDEO</h3>
    <p class="abs lesson-desc">Descraption of the video which is playing now Note that the video can play as full screen by the build in icon in video player which is playing now Note that the video can play as full screen by the build in icon in video player</p>
    <div class="abs lesson-item">
      <p>Descraption of the video which is playing now Note that the video can play as full screen by the build in icon in video player</p>
      <div class="row"><span>2.0: How to upload your file</span><span>13:05</span></div>
    </div>
  </section>

  <section class="coach">
    <svg class="abs coach-photo" width="260" height="270" viewBox="0 0 260 270" role="img" aria-label="Black and white photo of the instructor in a striped shirt with arms crossed">
      <defs>
        <linearGradient id="coachTone" x1="0" y1="0" x2="1" y2="1">
          <stop offset="0" stop-color="#3a3a3a"/><stop offset=".5" stop-color="#9a9a9a"/><stop offset="1" stop-color="#5a5a5a"/>
        </linearGradient>
      </defs>
      <polygon points="40,40 100,20 160,10 200,50 250,170 230,220 170,270 110,260 50,245 5,130" fill="url(#coachTone)"/>
    </svg>
    <p class="abs coach-kicker">to Know the</p>
    <h2 class="abs coach-role">INESTRACTOR</h2>
    <p class="abs coach-name">Mark <b>ELLISON</b></p>
    <svg class="abs coach-stars" width="80" height="26" viewBox="0 0 80 26">
      <g fill="#f5c21b" stroke="#d99a0a" stroke-width="1">
        <polygon points="12,1 15,9 24,9 17,15 19,24 12,19 5,24 7,15 0,9 9,9"/>
        <polygon points="38,1 41,9 50,9 43,15 45,24 38,19 31,24 33,15 26,9 35,9"/>
        <polygon points="64,1 67,9 76,9 69,15 71,24 64,19 57,24 59,15 52,9 61,9"/>
      </g>
    </svg>
    <p class="abs coach-bio">Descraption of the video which is playing now Note that the video can play as full screen by the build in icon in video player Descraption of the video which is playing now Note that the video can play as full screen by the build in icon in video player</p>
    <a class="abs coach-link" href="#">like to know other inestractors</a>
  </section>

  <footer class="abs footer">
    <div class="social"><span></span><span></span><span></span><span></span><span></span><span></span></div>
    <p class="copyright">All copyrights resereved by yourcompnay @2018</p>
  </footer>

</main>
</body>
</html>
```